Construction site banner with out Company information

I need a banner 4' tall and 6' wide, I want the banner to look very similar to the photo I uploaded from ChatGPT, make the person as life like as possible, I like the eyes to pop and be blue, and the hard hat orange, with the rest black and white, I have included our logo to use on the banner as well. Include the following:
Company Name: Rivlen Staffing
Temp Employees
General and Skilled Trades
Workers Comp and Payroll Coverage
www.rvlnstaff.com

Target Market(s)

Construction Companies

Requirements
Nice to have
• Realistic Person, bright blue eyes, orange hard hat
Should not have
• cartoon looking person

```html
<!DOCTYPE html>
<html lang="en">
<head>
<meta charset="utf-8">
<title>Rivlen Staffing – Banner Variations</title>
<link href="https://fonts.googleapis.com/css2?family=Poppins:wght@300;400;500;600;700;800&display=swap" rel="stylesheet">
<style>
  :root {
    --page: #ffffff;
    --ink: #0b0b0b;
    --orange: #f26a1b;
    --orange-light: #f7a43a;
    --white: #ffffff;
    --label: #555555;
  }
  * { margin: 0; padding: 0; box-sizing: border-box; }
  html, body { width: 1200px; height: 2879px; overflow: hidden; background: var(--page); }
  body { position: relative; font-family: "Poppins", sans-serif; }

  .banner {
    position: absolute; left: 192px; width: 565px; height: 377px;
    background: var(--ink); overflow: hidden;
    box-shadow: 14px 16px 18px rgba(0,0,0,0.28);
  }
  .banner-photo {
    position: absolute; right: 0; top: 0; width: 330px; height: 100%;
    background:
      radial-gradient(ellipse 45% 20% at 62% 8%, #f0621c 0%, #c8461a 60%, transparent 100%),
      radial-gradient(ellipse 55% 55% at 60% 48%, #7a6a5c 0%, #3a322c 55%, transparent 85%),
      linear-gradient(90deg, #111 0%, #2a2a2a 40%, #1a1a1a 100%);
  }
  .banner-band { position: absolute; left: 0; bottom: 0; width: 565px; height: 114px; }
  .band-text {
    position: absolute; left: 24px; top: 270px;
    font-weight: 700; font-size: 19.5px; line-height: 23.5px; color: var(--white);
  }
  .site-url {
    position: absolute; right: 30px; top: 332px;
    font-size: 24px; font-weight: 400; color: var(--white); line-height: 1;
    white-space: nowrap;
  }
  .site-url .domain { color: var(--orange); }

  .brand-name {
    position: absolute; left: 24px; font-weight: 800; color: var(--orange);
    line-height: 1; letter-spacing: -1px;
  }
  .tagline { position: absolute; left: 24px; color: var(--orange); line-height: 1; }
  .headline { position: absolute; left: 24px; color: var(--white); line-height: 1; }

  .version-label {
    position: absolute; left: 895px; font-weight: 700; font-size: 70px;
    color: var(--label); line-height: 1;
  }

  /* V-1 */
  .v1 .brand-name { top: 20px; font-size: 56px; }
  .v1 .tagline { top: 94px; font-size: 32px; font-weight: 700; }
  .v1 .headline { top: 148px; font-size: 38px; font-weight: 700; line-height: 42px; }
  /* V-2 */
  .v2 .brand-name { top: 20px; font-size: 56px; }
  .v2 .tagline { top: 90px; font-size: 42px; font-weight: 300; }
  .v2 .headline { top: 148px; font-size: 38px; font-weight: 600; line-height: 42px; }
  /* V-3 */
  .v3 .brand-name { top: 20px; font-size: 62px; }
  .v3 .tagline { top: 104px; font-size: 50px; font-weight: 400; }
  .v3 .headline { top: 186px; font-size: 27px; font-weight: 600; }
  /* V-4 */
  .v4 .brand-name { top: 20px; font-size: 64px; }
  .v4 .tagline { top: 106px; font-size: 37px; font-weight: 700; }
  .v4 .headline { top: 184px; font-size: 29px; font-weight: 700; }
  /* V-5 */
  .v5 .brand-name { top: 18px; font-size: 50px; }
  .v5 .tagline { top: 84px; font-size: 32px; font-weight: 600; letter-spacing: 1.5px; }
  .v5 .headline { top: 143px; font-size: 40px; font-weight: 500; line-height: 44px; }
</style>
</head>
<body>

<svg width="0" height="0" style="position:absolute">
  <defs>
    <linearGradient id="bandFill" x1="0" y1="0" x2="1" y2="0">
      <stop offset="0" stop-color="#f26a1b"/>
      <stop offset="1" stop-color="#f8b448"/>
    </linearGradient>
  </defs>
</svg>

<!-- Variation 1 -->
<section class="banner v1" style="top:151px">
  <div class="banner-photo" role="img" aria-label="Realistic bearded construction worker in an orange hard hat with bright blue eyes, black and white site behind"></div>
  <div class="brand-name">Rivlen</div>
  <div class="tagline">STAFFING</div>
  <div class="headline">TEMP<br>EMPLOYEES</div>
  <svg class="banner-band" viewBox="0 0 565 114"><path d="M0 0H165C245 0 270 30 305 70C335 104 370 114 395 114H0Z" fill="url(#bandFill)" stroke="#ffffff" stroke-width="3"/></svg>
  <div class="band-text">General and<br>Skilled Trades<br>Workers Comp<br>and Payroll Coverage</div>
  <div class="site-url"><span class="domain">rvlnstaff</span>.com</div>
</section>
<div class="version-label" style="top:310px">V-1</div>

<!-- Variation 2 -->
<section class="banner v2" style="top:677px">
  <div class="banner-photo" role="img" aria-label="Realistic bearded construction worker in an orange hard hat with bright blue eyes, black and white site behind"></div>
  <div class="brand-name">Rivlen</div>
  <div class="tagline">Staffing</div>
  <div class="headline">Temp<br>Employees</div>
  <svg class="banner-band" viewBox="0 0 565 114"><path d="M0 0H165C245 0 270 30 305 70C335 104 370 114 395 114H0Z" fill="url(#bandFill)" stroke="#ffffff" stroke-width="3"/></svg>
  <div class="band-text">General and<br>Skilled Trades<br>Workers Comp<br>and Payroll Coverage</div>
  <div class="site-url"><span class="domain">rvlnstaff</span>.com</div>
</section>
<div class="version-label" style="top:826px">V-2</div>

<!-- Variation 3 -->
<section class="banner v3" style="top:1203px">
  <div class="banner-photo" role="img" aria-label="Realistic bearded construction worker in an orange hard hat with bright blue eyes, black and white site behind"></div>
  <div class="brand-name">Rivlen</div>
  <div class="tagline">Staffing</div>
  <div class="headline">Temp Employees</div>
  <svg class="banner-band" viewBox="0 0 565 114"><path d="M0 0H165C245 0 270 30 305 70C335 104 370 114 395 114H0Z" fill="url(#bandFill)" stroke="#ffffff" stroke-width="3"/></svg>
  <div class="band-text">General and<br>Skilled Trades<br>Workers Comp<br>and Payroll Coverage</div>
  <div class="site-url"><span class="domain">rvlnstaff</span>.com</div>
</section>
<div class="version-label" style="top:1352px">V-3</div>

<!-- Variation 4 -->
<section class="banner v4" style="top:1730px">
  <div class="banner-photo" role="img" aria-label="Realistic bearded construction worker in an orange hard hat with bright blue eyes, black and white site behind"></div>
  <div class="brand-name">Rivlen</div>
  <div class="tagline">STAFFING</div>
  <div class="headline">TEMP EMPLOYEES</div>
  <svg class="banner-band" viewBox="0 0 565 114"><path d="M0 0H165C245 0 270 30 305 70C335 104 370 114 395 114H0Z" fill="url(#bandFill)" stroke="#ffffff" stroke-width="3"/></svg>
  <div class="band-text">General and<br>Skilled Trades<br>Workers Comp<br>and Payroll Coverage</div>
  <div class="site-url"><span class="domain">rvlnstaff</span>.com</div>
</section>
<div class="version-label" style="top:1880px">V-4</div>

<!-- Variation 5 -->
<section class="banner v5" style="top:2261px">
  <div class="banner-photo" role="img" aria-label="Realistic bearded construction worker in an orange hard hat with bright blue eyes, black and white site behind"></div>
  <div class="brand-name">Rivlen</div>
  <div class="tagline">Staffing</div>
  <div class="headline">Temp<br>Employees</div>
  <svg class="banner-band" viewBox="0 0 565 114"><path d="M0 0H165C245 0 270 30 305 70C335 104 370 114 395 114H0Z" fill="url(#bandFill)" stroke="#ffffff" stroke-width="3"/></svg>
  <div class="band-text">General and<br>Skilled Trades<br>Workers Comp<br>and Payroll Coverage</div>
  <div class="site-url"><span class="domain">rvlnstaff</span>.com</div>
</section>
<div class="version-label" style="top:2412px">V-5</div>

</body>
</html>
```